Larkfield Circuitry LLC is a Minneapolis / St Paul and surrounding communities computer repair and service company. It serves residential and small businesses. We work primarily with virus removal, data recovery, system baselines, networking, and new system installation. The site should look clean, professional, and easy to navigate.

This wordpress project must be coded and integrated into a wordpress theme for easy upload and maintenance.
Updates

Designers - Please make sure your design is in a wordpress theme so that It can be uploaded.  

Thank you,

Brin 

Target Market(s)

Residential and Small Business

Industry/Entity Type

Residential

Requirements
Must have
• Site Content
1. Main Page should have photos that scroll across, Business Description, Space to run
“Specials” Ads
a. Intuitive Navigation
2. Additional Pages
a. Blog for Computer Repair Articles
b. Testimonials Page
c. Contact Pages
d. Services Page with the ability to put in pricing
3. The site must be clean and professional.
4. Wordpress Theme

```html
<!DOCTYPE html>
<html lang="en">
<head>
<meta charset="utf-8">
<title>Larkfield Circuitry LLC – Computer Repair &amp; Service</title>
<link href="https://fonts.googleapis.com/css2?family=Montserrat:wght@500;600;700&family=Open+Sans:ital,wght@0,400;1,400&family=Roboto+Slab:wght@400&display=swap" rel="stylesheet">
<style>
  :root{
    --green:#4f9e2d;
    --green-dark:#3d8a1f;
    --red:#ee1c1c;
    --ink:#333333;
    --muted:#555555;
    --nav-ink:#444444;
    --panel:#eeeeee;
    --ad:#dddddd;
    --ad-ink:#a0a0a0;
    --footer:#4a4a4a;
    --white:#ffffff;
    --black:#0d0d0d;
  }
  *{margin:0;padding:0;box-sizing:border-box}
  html,body{width:1200px;height:874px;overflow:hidden;background:var(--white)}
  body{position:relative;font-family:"Open Sans",Arial,sans-serif;color:var(--ink)}

  .site-header{position:absolute;left:0;top:0;width:1200px;height:118px;
    background:linear-gradient(#ffffff 0%,#ffffff 45%,#ececec 100%);
    border-bottom:1px solid #d4d4d4}
  .brand{position:absolute;left:141px;top:30px;display:flex;align-items:center;gap:12px}
  .brand-mark{width:40px;height:40px;border-radius:50%;background:var(--green)}
  .brand-name{font-family:"Montserrat",sans-serif;font-weight:700;font-size:30px;color:#3a3a3a;letter-spacing:-0.5px}

  .contact-info{position:absolute;left:835px;top:20px}
  .contact-info svg{position:absolute;left:0;top:0}
  .phone{position:absolute;left:60px;top:0;font-family:"Open Sans",sans-serif;font-size:29px;color:var(--red);white-space:nowrap;letter-spacing:0.5px}
  .email{position:absolute;left:62px;top:27px;font-size:15px;color:#555;white-space:nowrap;margin-top:2px}

  .main-nav{position:absolute;top:85px;left:0;width:1200px;height:31px}
  .main-nav a{position:absolute;top:0;height:31px;line-height:31px;font-family:"Montserrat",sans-serif;font-weight:500;font-size:14.5px;color:var(--nav-ink);text-decoration:none;text-transform:uppercase}
  .main-nav a.active{background:var(--green);color:var(--white);padding:0 12px}

  .hero{position:absolute;left:0;top:118px;width:1200px;height:419px;
    background:linear-gradient(#f3f3f3,#fafafa 60%,#efefef);border-bottom:1px solid #d8d8d8}
  .hero-person{position:absolute;left:204px;top:38px;width:252px;height:222px;
    background:linear-gradient(#d9d2cc,#3e4450 70%,#2d3340)}
  .hero-product{position:absolute;left:625px;top:62px;width:384px;height:325px;
    background:radial-gradient(ellipse at 45% 45%,#5a5a5a,#9ea3a8 65%,#e6e6e6)}
  .caption{position:absolute;left:141px;font-family:"Roboto Slab",serif;font-size:20px;color:var(--white);padding:0 13px;height:29px;line-height:29px;white-space:nowrap}
  .caption.dark{top:260px;background:var(--black);width:365px}
  .caption.green{top:293px;background:var(--green);width:422px}
  .slider-dots{position:absolute;left:932px;top:384px;display:flex;gap:9px}
  .slider-dots span{width:17px;height:17px;border-radius:50%;background:var(--white);border:2px solid #dcdcdc}
  .slider-dots span.current{background:var(--green);border-color:#dcdcdc}

  .welcome{position:absolute;left:141px;top:573px;width:603px;height:208px;background:var(--panel);border-left:4px solid var(--green);padding:14px 22px 0 19px}
  .welcome h1{font-family:"Roboto Slab",serif;font-weight:400;font-size:25px;color:var(--green)}
  .welcome p{font-size:12.5px;line-height:19px;color:var(--muted);margin-top:14px}
  .welcome .read-more{position:absolute;left:19px;top:170px;font-size:11px;font-style:italic;color:var(--red);text-decoration:none}

  .ad-banner{position:absolute;left:778px;top:573px;width:281px;height:208px;background:var(--ad);display:flex;align-items:center;justify-content:center;text-align:center;font-style:italic;font-size:22px;line-height:26px;color:var(--ad-ink);text-transform:uppercase}

  .site-footer{position:absolute;left:0;top:835px;width:1200px;height:39px;background:var(--footer);color:var(--white);font-size:12.5px}
  .footer-links{position:absolute;left:143px;top:10px}
  .footer-links a{color:var(--white);text-decoration:none}
  .copyright{position:absolute;right:143px;top:11px;font-size:11.5px}
</style>
</head>
<body>
  <header class="site-header">
    <div class="brand">
      <span class="brand-mark"></span>
      <span class="brand-name">Larkfield Circuitry LLC</span>
    </div>
    <div class="contact-info">
      <svg width="46" height="40" viewBox="0 0 46 40" aria-hidden="true">
        <polygon points="4,8 40,4 42,30 6,34" fill="#2e9fd8"/>
        <polyline points="4,8 24,20 40,4" fill="none" stroke="#1a6fa3" stroke-width="2"/>
        <circle cx="8" cy="34" r="5" fill="#f5a623"/>
      </svg>
      <div class="phone">555 014 2290</div>
      <div class="email">info@larkfieldcircuitry.com</div>
    </div>
    <nav class="main-nav">
      <a class="active" href="#" style="left:507px">Home</a>
      <a href="#" style="left:587px">About Us</a>
      <a href="#" style="left:686px">Services</a>
      <a href="#" style="left:781px">Blog</a>
      <a href="#" style="left:848px">Testimonials</a>
      <a href="#" style="left:977px">Contact</a>
    </nav>
  </header>

  <section class="hero">
    <div class="hero-person" role="img" aria-label="Photo of a smiling businessman in a suit"></div>
    <div class="hero-product" role="img" aria-label="Photo of a computer tower with a wrench and screwdriver"></div>
    <div class="caption dark">There are many variation of passage</div>
    <div class="caption green">Standard dummy text ever since the 1500s</div>
    <div class="slider-dots">
      <span class="current"></span><span></span><span></span><span></span><span></span>
    </div>
  </section>

  <section class="welcome">
    <h1>Welcome to Larkfield Circuitry</h1>
    <p>Larkfield Circuitry LLC is a Minneapolis / St Paul and surrounding communities computer repair and service company. It serves residential and small businesses.</p>
    <p>We work primarily with virus removal, data recovery, system baselines, networking, and new system installation. The site should look clean, professional, and easy to navigate.</p>
    <a class="read-more" href="#">Read More...</a>
  </section>

  <aside class="ad-banner">Advertisement<br>Banner</aside>

  <footer class="site-footer">
    <div class="footer-links">
      <a href="#">Home</a> | <a href="#">About us</a> | <a href="#">Services</a> | <a href="#">Blog</a> | <a href="#">Testimonials</a> | <a href="#">Contact</a>
    </div>
    <div class="copyright">Copyright © 2012 Larkfield Circuitry. All Rights Reserved.</div>
  </footer>
</body>
</html>
```